Book cover for book about Climate Change

Looking for a clean, bold, and attractive cover for a mass-market paperback (5.5"x 8.5") about solving the climate change problem. Title is either "When Rivers Learn to Sing” or A Lantern Over Quiet Fields” (your choice), subtitle is "A five-step plan to reverse climate change — to ensure that your grandchildren will live on a clean and comfortable planet," author is Dale Pruitt. Thinking that it *might* feature an image of Earth (or a portion thereof) and its very thin layer of atmosphere -- but STRONGLY encourage other ideas too!

Requirements
Nice to have
• Keep it positive — NOT scary doom-and-gloom

```html
<!DOCTYPE html>
<html lang="en">
<head>
<meta charset="utf-8">
<title>A Lantern Over Quiet Fields — Dale Pruitt</title>
<link rel="stylesheet" href="https://fonts.googleapis.com/css2?family=Jost:wght@300;400;500;600&display=swap">
<style>
  :root {
    --orange: #ff9212;
    --paper: #f7f7f7;
    --navy: #15266f;
    --globe-light: #8a8a8a;
    --globe-dark: #262626;
  }
  html, body {
    margin: 0;
    padding: 0;
    width: 776px;
    height: 1200px;
    overflow: hidden;
    background: var(--orange);
  }
  .cover {
    position: relative;
    width: 776px;
    height: 1200px;
    overflow: hidden;
    background: var(--orange);
    font-family: "Jost", sans-serif;
  }
  .cover__art {
    position: absolute;
    inset: 0;
  }
  .cover__title {
    position: absolute;
    left: 64px;
    top: 257px;
    margin: 0;
    color: var(--navy);
    font-family: "Jost", sans-serif;
    font-weight: 500;
    font-size: 118px;
    line-height: 124px;
    letter-spacing: 0.01em;
    text-transform: uppercase;
  }
  .cover__title span {
    display: block;
    white-space: nowrap;
  }
  .cover__subtitle {
    position: absolute;
    left: 71px;
    top: 890px;
    width: 640px;
    margin: 0;
    color: var(--navy);
    font-family: "Jost", sans-serif;
    font-weight: 300;
    font-size: 35px;
    line-height: 45px;
    white-space: nowrap;
  }
  .cover__subtitle strong {
    font-weight: 500;
  }
  .cover__author {
    position: absolute;
    left: 0;
    right: 0;
    top: 1123px;
    margin: 0;
    text-align: center;
    color: var(--paper);
    font-family: "Jost", sans-serif;
    font-weight: 400;
    font-size: 27px;
    line-height: 1;
    letter-spacing: 0.72em;
    text-indent: 0.72em;
    text-transform: uppercase;
  }
</style>
</head>
<body>
  <main class="cover">
    <svg class="cover__art" width="776" height="1200" viewBox="0 0 776 1200">
      <defs>
        <radialGradient id="globe-shade" cx="0.38" cy="0.35" r="0.7">
          <stop offset="0" stop-color="var(--globe-light)"/>
          <stop offset="1" stop-color="var(--globe-dark)"/>
        </radialGradient>
      </defs>
      <circle class="sun-disc" cx="228" cy="427" r="316" fill="var(--paper)"/>
      <circle class="globe" cx="575" cy="140" r="236" fill="url(#globe-shade)"
              role="img" aria-label="Black-and-white satellite view of Earth showing the Americas under swirling clouds"/>
    </svg>

    <h1 class="cover__title">
      <span>A</span>
      <span>Lantern</span>
      <span>Over</span>
      <span>Quiet</span>
      <span>Fields</span>
    </h1>

    <p class="cover__subtitle">A <strong>five-step plan to reverse climate<br>change,</strong> to ensure that your<br>grandchildren will live on a clean<br>and comfortable planet.</p>

    <p class="cover__author">Dale Pruitt</p>
  </main>
</body>
</html>
```